Email Signature

brimLake Technology is in need of updating our email signature block. We are a technology firm that specializes in cloud services and infrastructure. We would like something that includes, name, title, office addresses (We currently have 3 locations), phone, cell, email and website. We are open to having a logo and motto and looking for something that we can roll out with the new year that is very eye catching.

Industry/Entity Type

Office

Font styles to use
Sans Serif

Requirements
Must have
• Employee name, title, office addresses (We currently have 3 locations), phone, cell, email and website

```html
<!DOCTYPE html>
<html lang="en">
<head>
<meta charset="utf-8">
<title>brimLake Technology – Email Signature</title>
<link rel="stylesheet" href="https://fonts.googleapis.com/css2?family=Source+Sans+3:ital,wght@0,400;0,600;1,400&display=swap">
<style>
  :root {
    --page: #ffffff;
    --ink: #2f2f2f;
    --ink-soft: #4a4a4a;
    --accent: #f26b1d;
    --rule: #555555;
  }
  * { margin: 0; padding: 0; box-sizing: border-box; }
  html, body {
    width: 1200px;
    height: 1000px;
    overflow: hidden;
    background: var(--page);
    font-family: "Source Sans 3", Arial, sans-serif;
    color: var(--ink-soft);
  }
  .signature {
    position: absolute;
    left: 100px;
    top: 340px;
    width: 1000px;
    height: 300px;
  }
  .identity { position: absolute; left: 0; top: 0; }
  .identity__name {
    font-size: 44px;
    font-weight: 400;
    color: var(--ink);
    line-height: 1.1;
  }
  .identity__title {
    font-size: 26px;
    font-style: italic;
    color: var(--ink-soft);
    margin-top: 4px;
  }
  .brand {
    position: absolute;
    left: 600px;
    top: 2px;
    width: 380px;
    text-align: center;
  }
  .brand__lockup {
    display: flex;
    align-items: center;
    justify-content: center;
    gap: 12px;
  }
  .brand__mark {
    width: 34px;
    height: 34px;
    border-radius: 50%;
    background: var(--accent);
  }
  .brand__name {
    font-size: 34px;
    font-weight: 400;
    color: var(--ink);
    line-height: 1;
  }
  .brand__motto {
    font-size: 15px;
    font-style: italic;
    color: var(--ink-soft);
    margin-top: 12px;
    white-space: nowrap;
  }
  .contact {
    position: absolute;
    left: 0;
    top: 120px;
    font-size: 22px;
    line-height: 36px;
  }
  .contact__label { color: var(--accent); }
  .contact__sep { margin: 0 14px; color: var(--ink-soft); }
  .offices {
    position: absolute;
    left: 0;
    top: 218px;
    display: flex;
    font-size: 20px;
    line-height: 27px;
  }
  .office { padding-right: 18px; }
  .office + .office {
    border-left: 2px solid var(--rule);
    padding-left: 16px;
  }
  .office__name { color: var(--accent); }
</style>
</head>
<body>
  <section class="signature">
    <div class="identity">
      <h1 class="identity__name">Daniel Reyes</h1>
      <p class="identity__title">managing Director</p>
    </div>

    <div class="brand">
      <div class="brand__lockup">
        <span class="brand__mark"></span>
        <span class="brand__name">brimLake Technology</span>
      </div>
      <p class="brand__motto">Dependable cloud and infrastructure for every growing team</p>
    </div>

    <div class="contact">
      <p><span class="contact__label">Phone:</span> 555-014-2290<span class="contact__sep">|</span><span class="contact__label">Cell:</span> 555-014-2290</p>
      <p><span class="contact__label">Email:</span> hello@brimlaketech.com<span class="contact__sep">|</span><span class="contact__label">Web:</span> www.brimlaketech.com</p>
    </div>

    <div class="offices">
      <div class="office">
        <p class="office__name">Corporate Office:</p>
        <p>4820 N. Canyon Ridge Road,</p>
        <p>Suite 210, Tempe, AZ 85281</p>
      </div>
      <div class="office">
        <p class="office__name">Network Operating Center:</p>
        <p>932 W. Larkspur Ave, Suite 1407,</p>
        <p>Mesa, AZ 85201</p>
      </div>
      <div class="office">
        <p class="office__name">Austin Office:</p>
        <p>1150 Meadow Park Boulevard,</p>
        <p>Suite 500, Austin, Texas, 78701</p>
      </div>
    </div>
  </section>
</body>
</html>
```